4-Page Brochure for Harbor Renewals

Harbor Renewals is a multi-faceted company established by a board certified
physician with over 20 years of experience. We assist our clients in naturally optimizing their wellness and appearance through a holistic approach which includes:(1) a personalized, medically-supervised weight loss program, (2) cosmetic body treatments such as lipolaser, cool sculpting, radio frequency and ultrasound cavitation, skin tightening, lifting. We can reduce double chin, acne scars, facial wrinkles and blemishes. Our state of the art machines can reduce cellulite. and skin dimpling physician-formulated vitamins, supplements, nutraceuticals and skin care products which will be offered in our medical offices and online nationally, and (4) vitamin and mineral-enhanced beverage products which will also be offered in our offices as well as online nationally. We want our improve the way our clients feel, as well as how they look.
Design Specifics: We think a design which in some way represents the human body/form would be most representative of our company's mission. We do not want to use pink, as our products and services are designed for both genders. Other than that, we are open to different color schemes. We wouldn't use flowery script-type or very informal fonts, but rather something more professional looking.
Target Market(s)
man and women age 30 Plus
Industry/Entity Type
It Company
Contact Information for Business Card
I have attached a logo of my company " Harbor Renewals: Card must have it
Requirements
Must have
- Logo that I submitted,

```html
<!DOCTYPE html>
<html lang="en">
<head>
<meta charset="utf-8">
<title>Harbor Renewals – Flyer</title>
<link href="https://fonts.googleapis.com/css2?family=Oswald:wght@300;400&family=Questrial&display=swap" rel="stylesheet">
<style>
:root{
  --page-bg:#e9e8ec;
  --paper:#ffffff;
  --sky:#29abe2;
  --sky-light:#5cc3ee;
  --lavender:#a99ad0;
  --lavender-soft:#d9d3ec;
  --lavender-mist:#eeebf6;
  --purple:#6a4aa8;
  --purple-deep:#4b2d8f;
  --ink:#3d3d44;
  --skin-light:#f1d2bf;
  --skin-mid:#d9a27f;
  --skin-tan:#b97a52;
  --skin-dark:#8a5535;
}
*{margin:0;padding:0;box-sizing:border-box}
html,body{width:1125px;height:1200px;overflow:hidden;background:var(--page-bg)}
.flyer{
  position:absolute;left:165px;top:40px;width:621px;height:876px;
  transform:scale(1.2785);transform-origin:0 0;
  background:linear-gradient(180deg,var(--paper) 0%,var(--paper) 55%,var(--lavender-mist) 100%);
  overflow:hidden;font-family:"Questrial",sans-serif;
}
.abs{position:absolute}
.backdrop{position:absolute;inset:0}
.photo-faces{left:0;top:0;width:306px;height:330px;
  background:linear-gradient(90deg,var(--skin-light) 0%,#f3dccd 35%,#ead0c0 70%,rgba(255,255,255,0) 100%)}
.photo-figure{left:505px;top:10px;width:116px;height:290px;
  background:radial-gradient(ellipse 50% 55% at 50% 55%,var(--skin-tan) 0%,var(--skin-mid) 55%,rgba(255,255,255,0) 100%)}
.brand{left:288px;top:114px;display:flex;align-items:center;gap:7px}
.brand-dot{width:48px;height:48px;border-radius:50%;background:var(--sky);flex:none}
.brand-name{font-size:21px;color:var(--lavender);line-height:1;white-space:nowrap}
.bubble{border-radius:50%;border:5px solid var(--lavender);background:#fff;padding:3px}
.bubble-photo{width:100%;height:100%;border-radius:50%}
.bubble-waist{left:54px;top:258px;width:152px;height:152px}
.bubble-waist .bubble-photo{background:radial-gradient(ellipse 50% 60% at 50% 40%,var(--skin-tan),var(--skin-dark) 60%,#1c1412 100%)}
.bubble-hips{left:230px;top:322px;width:150px;height:150px}
.bubble-hips .bubble-photo{background:radial-gradient(ellipse 55% 55% at 55% 55%,var(--skin-mid),var(--skin-tan) 60%,#fff 100%)}
.bubble-face{left:418px;top:390px;width:160px;height:160px}
.bubble-face .bubble-photo{background:radial-gradient(ellipse 50% 60% at 50% 50%,var(--skin-light),#e7c0a6 60%,#fff 100%)}
.headline{left:46px;top:534px;font-family:"Oswald",sans-serif;font-weight:400;text-transform:uppercase;line-height:1.22}
.headline span{display:block}
.headline-1{font-size:15.5px;color:var(--purple-deep)}
.headline-2{font-size:17.5px;color:var(--purple-deep)}
.headline-3{font-size:22.5px;color:var(--sky)}
.intro{left:46px;top:628px;width:380px;font-size:14.3px;line-height:18px;color:var(--purple);white-space:nowrap}
.services{left:46px;top:671px;width:560px;list-style:none;font-size:11.3px;line-height:15px;color:var(--ink)}
.services li{position:relative;padding-left:18px;margin-bottom:7px}
.services li.narrow{width:370px}
.services li::before{content:"";position:absolute;left:3px;top:2px;width:10px;height:10px;border-radius:50%;
  background:linear-gradient(90deg,var(--lavender) 50%,var(--sky) 50%)}
.contact{left:436px;top:561px;width:156px;height:230px;border:3px solid var(--lavender);
  background:linear-gradient(180deg,rgba(233,221,214,.75),rgba(255,255,255,.92) 45%);text-align:center;color:var(--ink)}
.contact-call{margin-top:50px;font-family:Arial,sans-serif;font-size:19px;line-height:22px}
.contact-call span{display:block;font-size:22px}
.contact-phone{margin-top:12px;display:flex;justify-content:center;align-items:center;gap:6px;font-size:15px}
.contact-heading{margin-top:14px;font-size:16px}
.contact-address{font-size:13px;line-height:16px}
.contact-web{margin-top:8px;font-size:10.5px;display:flex;justify-content:center;align-items:center;gap:4px}
.contact-web::before{content:"";width:6px;height:6px;border-radius:50%;background:var(--purple)}
</style>
</head>
<body>
<main class="flyer">
  <div class="abs photo-faces" role="img" aria-label="Three women's faces showing the stages of skin ageing"></div>
  <div class="abs photo-figure" role="img" aria-label="Woman with a toned figure in black sportswear"></div>

  <svg class="backdrop" viewBox="0 0 621 876" width="621" height="876" aria-hidden="true">
    <polygon points="0,428 380,546 0,546" fill="var(--lavender-soft)"/>
    <polygon points="0,188 621,395 621,613 0,428" fill="var(--sky)"/>
    <polygon points="0,188 300,288 0,330" fill="var(--sky-light)" opacity=".5"/>
    <polygon points="386,302 621,228 621,380" fill="var(--lavender)" opacity=".85"/>
    <polygon points="0,428 260,509 0,520" fill="var(--lavender)" opacity=".7"/>
  </svg>

  <div class="abs brand">
    <span class="brand-dot"></span>
    <span class="brand-name">Harbor Renewals</span>
  </div>

  <div class="abs bubble bubble-waist"><div class="bubble-photo" role="img" aria-label="Slim waist in white underwear"></div></div>
  <div class="abs bubble bubble-hips"><div class="bubble-photo" role="img" aria-label="Toned hips in nude underwear"></div></div>
  <div class="abs bubble bubble-face"><div class="bubble-photo" role="img" aria-label="Older woman's face with a skin-lifting effect"></div></div>

  <h1 class="abs headline">
    <span class="headline-1">We are multi-faceted company established</span>
    <span class="headline-2">By a board certified physician with</span>
    <span class="headline-3">Over 20 years of experience.</span>
  </h1>

  <p class="abs intro">We assist our clients in naturally optimizing their wellness<br>&amp; appearance through a holistic approach which includes:</p>

  <ul class="abs services">
    <li class="narrow">A personalized, medically-supervised weight loss program.</li>
    <li class="narrow">Cosmetic body treatments such as lipolaser, cool sculpting, radio frequency and ultrasound cavitation, skin tightening, lifting. We can reduce double chin, acne scars, facial wrinkles and blemishes.</li>
    <li class="narrow">Our state of the art machines can reduce cellulite. and skin dimpling physician-formulated vitamins, supplements, nutraceuticals and skin care products which will be offered in our medical offices and online nationally.</li>
    <li>Our state of the art machines can reduce cellulite. and skin dimpling physician-formulated vitamins, supplements, nutraceuticals and skin care products which will be offered in our medical offices and online nationally.</li>
  </ul>

  <aside class="abs contact">
    <p class="contact-call">CALL US<span>TODAY</span></p>
    <p class="contact-phone">
      <svg width="16" height="16" viewBox="0 0 16 16" aria-hidden="true"><circle cx="8" cy="8" r="7" fill="none" stroke="var(--purple)" stroke-width="1.5"/><path d="M5.5 4.5l1.3 1.6-.7 1a5 5 0 0 0 2.8 2.8l1-.7 1.6 1.3-.8 1.2c-3 0-6-3-6.2-6z" fill="var(--purple)"/></svg>
      123-555-0148
    </p>
    <p class="contact-heading">Contact Info</p>
    <p class="contact-address">Address Line 1<br>Address Line 2</p>
    <p class="contact-web">www.harborrenewals.com</p>
  </aside>
</main>
</body>
</html>
```